Business card to be used as a flyer

This business card should do the trick of a full scale flyer , so basicaly from the business card itself we only keep the size and remove the clasical name , position , company name (etc).
This business cards should be , like said above, used as promo tool, being gived to different girls . So base one : the design is girls oriented.
Colors : black background . We will use gold (color) folio for the text.
Attached you have our logo, but this should not be a proiminent part of the design . You can use only the cat head instead.
Target Market(s)
Girls / Women
Contact Information for Business Card
> black background , gold / folio text and elements
> cat head from the logo in a creative way do be displayed
> proieminent text "your path to success starts here"
> contact details phone and website .
www.velmastrand.ro (website) and 0742163958 (phone)

```html
<!DOCTYPE html>
<html lang="en">
<head>
<meta charset="utf-8">
<title>Velmastrand – Your path to Success</title>
<link href="https://fonts.googleapis.com/css2?family=Great+Vibes&family=Montserrat:wght@400&display=swap" rel="stylesheet">
<style>
  :root {
    --card-black: #000000;
    --decor-grey: #1e1e1e;
    --decor-grey-soft: rgba(30, 30, 30, 0.55);
    --gold-light: #fff1a8;
    --gold-mid: #e8c45a;
    --gold-deep: #b8872a;
    --contact-white: #f2f2f2;
  }
  html, body {
    margin: 0;
    padding: 0;
    overflow: hidden;
    background: var(--card-black);
  }
  .card {
    position: relative;
    width: 1200px;
    height: 686px;
    background: var(--card-black);
    overflow: hidden;
  }
  .card__decor {
    position: absolute;
    left: 252px;
    top: 0;
    width: 766px;
    height: 634px;
    border-radius: 46% 54% 48% 52% / 30% 38% 62% 70%;
    background: radial-gradient(ellipse at 55% 45%, var(--decor-grey) 0%, var(--decor-grey-soft) 50%, rgba(0, 0, 0, 0) 78%);
  }
  .card__headline {
    position: absolute;
    left: 0;
    width: 100%;
    box-sizing: border-box;
    margin: 0;
    padding: 50px 60px 40px;
    font-family: "Great Vibes", cursive;
    font-weight: 400;
    font-size: 132px;
    text-align: center;
    line-height: 1.1;
    white-space: nowrap;
    background: linear-gradient(180deg, var(--gold-light) 0%, var(--gold-mid) 45%, var(--gold-deep) 72%, var(--gold-mid) 100%);
    -webkit-background-clip: text;
    background-clip: text;
    color: transparent;
  }
  .card__headline--first {
    top: 62px;
    left: -18px;
  }
  .card__headline--second {
    top: 200px;
    left: 0;
  }
  .contact {
    position: absolute;
    top: 448px;
    display: flex;
    align-items: center;
    gap: 12px;
    font-family: "Montserrat", sans-serif;
    font-size: 24px;
    color: var(--contact-white);
  }
  .contact--phone { left: 312px; }
  .contact--web { left: 592px; }
  .contact__icon {
    width: 39px;
    height: 39px;
    flex: none;
  }
</style>
</head>
<body>
  <main class="card">
    <div class="card__decor" role="img" aria-label="Large faint brand cat-head silhouette behind the headline"></div>

    <h1 class="card__headline card__headline--first">Your path to Success</h1>
    <p class="card__headline card__headline--second">Starts here</p>

    <div class="contact contact--phone">
      <svg class="contact__icon" viewBox="0 0 40 40" aria-hidden="true">
        <rect x="2" y="2" width="36" height="36" rx="7" fill="none" stroke="#e8c45a" stroke-width="2.5"/>
        <path d="M13 11c1-1 2.5-1 3.2 0l2 3c.6.9.3 1.9-.5 2.5l-1.2.9c.9 2.4 2.7 4.3 5.1 5.3l.9-1.2c.6-.8 1.7-1 2.5-.4l3 2c1 .7 1 2.2 0 3.2l-1.3 1.3c-1.3 1.3-3.4 1.5-5.1.6-4.6-2.3-8.3-6-10.5-10.6-.8-1.7-.6-3.7.7-5z" fill="none" stroke="#e8c45a" stroke-width="2" stroke-linejoin="round"/>
      </svg>
      <span class="contact__text">0742163958</span>
    </div>

    <div class="contact contact--web">
      <svg class="contact__icon" viewBox="0 0 40 40" aria-hidden="true">
        <rect x="2" y="2" width="36" height="36" rx="7" fill="none" stroke="#e8c45a" stroke-width="2.5"/>
        <circle cx="20" cy="20" r="9.5" fill="none" stroke="#e8c45a" stroke-width="2"/>
        <ellipse cx="20" cy="20" rx="4" ry="9.5" fill="none" stroke="#e8c45a" stroke-width="2"/>
        <line x1="10.5" y1="20" x2="29.5" y2="20" stroke="#e8c45a" stroke-width="2"/>
      </svg>
      <span class="contact__text">www.velmastrand.ro</span>
    </div>
  </main>
</body>
</html>
```